Template Invitation For Regular Meeting

Invitation to quarterly Tandem Kinfolk Trade Circle Exchange meeting. Needs to be e-mailed.

Target Market(s)

Family Business Owners

Industry/Entity Type

Business

Requirements
Must have
• Must be easy to e-mail.

```html
<!DOCTYPE html>
<html lang="en">
<head>
<meta charset="UTF-8">
<title>Tandem Kinfolk Trade Circle Exchange – Invitation</title>
<link rel="stylesheet" href="https://fonts.googleapis.com/css2?family=Barlow:wght@500;600;700&display=swap">
<style>
  :root {
    --brand-blue: #2a78b6;
    --band-blue-top: #1b87c8;
    --band-blue-bottom: #0a6dab;
    --leaf-light: #8cc866;
    --leaf-mid: #4f9a3a;
    --leaf-deep: #2f6e26;
    --soil: #5a3f2a;
    --white: #ffffff;
  }
  * { margin: 0; padding: 0; box-sizing: border-box; }
  html, body { width: 896px; height: 1200px; overflow: hidden; background: var(--white); }
  body { font-family: "Barlow", sans-serif; color: var(--white); }

  .invitation { position: relative; width: 896px; height: 1200px; background: var(--white); }

  .masthead {
    position: absolute; top: 0; left: 0; width: 896px; height: 183px;
    display: flex; align-items: center; justify-content: center; gap: 12px;
  }
  .masthead__mark { width: 18px; height: 18px; background: var(--brand-blue); }
  .masthead__name {
    font-size: 30px; font-weight: 700; color: var(--brand-blue); letter-spacing: 0.5px; line-height: 1;
  }

  .hero { position: absolute; top: 183px; left: 0; width: 896px; height: 422px; }
  .hero__photo {
    position: absolute; inset: 0;
    background:
      linear-gradient(180deg, rgba(0,0,0,0) 78%, var(--soil) 96%),
      radial-gradient(ellipse at 18% 15%, #b7dc95 0%, rgba(183,220,149,0) 45%),
      linear-gradient(90deg, var(--leaf-light) 0%, var(--leaf-mid) 50%, var(--leaf-deep) 100%);
  }
  .hero__text { position: absolute; top: 70px; left: 0; width: 100%; text-align: center; }
  .hero__heading {
    display: inline-block; font-size: 48px; font-weight: 700; line-height: 1;
    padding-bottom: 8px; border-bottom: 2px solid var(--white);
  }
  .hero__details { margin-top: 16px; font-size: 28px; font-weight: 500; line-height: 37.5px; }

  .program {
    position: absolute; top: 605px; left: 0; width: 896px; height: 472px; text-align: center;
    background: linear-gradient(180deg, var(--band-blue-top), var(--band-blue-bottom));
    font-size: 20.5px; font-weight: 500; letter-spacing: 0.3px;
  }
  .program__heading { margin-top: 28px; font-size: 31px; font-weight: 700; letter-spacing: 0.5px; }
  .program__item { margin-top: 22px; line-height: 27.5px; }
  .program__item--first { margin-top: 18px; }
  .program__item--tight { line-height: 23px; }

  .contact {
    position: absolute; top: 1111px; left: 0; width: 896px; text-align: center;
    color: var(--brand-blue); font-size: 21px; font-weight: 700; line-height: 28px; letter-spacing: 0.2px;
  }
</style>
</head>
<body>
<main class="invitation">
  <header class="masthead">
    <span class="masthead__mark" aria-hidden="true"></span>
    <span class="masthead__name">Tandem Kinfolk Trade Circle Exchange</span>
  </header>

  <section class="hero">
    <div class="hero__photo" role="img" aria-label="Photograph of young green seedlings sprouting from dark soil against a soft green background"></div>
    <div class="hero__text">
      <h1 class="hero__heading">YOU’RE INVITED!</h1>
      <p class="hero__details">October 18, 2017<br>8:00-10:30 a.m.<br>The Riverton Commons Club</p>
    </div>
  </section>

  <section class="program">
    <h2 class="program__heading">PROGRAM</h2>
    <p class="program__item program__item--first">7:30 a.m.&nbsp; Continental breakfast</p>
    <p class="program__item">8:00 "Next Gen" Panel:&nbsp; Developing Entrepreneurs in Every Generation.<br>
      Owen Hartley, Chief of Staff, Brightpane Windows.<br>
      Marcus Delaney, President, Summit Precision Machining Works, Inc.<br>
      Laura Whitfield, Vice President of Development, Golden Crust Bakeries, Inc.<br>
      Peter Rowan, Vice President of Operations, Northgate Services.</p>
    <p class="program__item">9:00 Break</p>
    <p class="program__item program__item--tight">9:20 Senior generation and Next Gen break-out<br>discussion groups and report-outs</p>
    <p class="program__item">10:30&nbsp; Close</p>
  </section>

  <footer class="contact">
    <p>For more information please call 555-013-2468</p>
    <p>www.kinfolkcircleriverton.com</p>
  </footer>
</main>
</body>
</html>
```